Unified Communications Product Brochure

I am a new startup Unified Communications as a Service company. I have a logo and some stock content that I need to use for a company brochure that highlights the product and company. I want it two to three pages max. I have uploaded a sample image, but want you to create a more professional image that is similar.

Target Market(s)

Businesses ranging from SMB to Enterprise. Our customers typically have a premises-based phone system that is aging and needs to be replaced. We replace on premises phone systems with a modern cloud based solution called TOLVARA Communications.

Industry/Entity Type

Telecommunications

Font styles to use
Sans Serif

Colors
ffffff
0355a3

Requirements
Must have
• I need a clean professional look that utilizes the image of the phone system I included. Below that I want to list the primary features. On the second page, I would like to list some problems we solve for business customers.
• Contact information must be included at the bottom of the last page.
Nice to have
• Image of the mobile app (both images I included). Image of redundant cloud datacenters to show the reliability and disaster recovery capabilities.
Should not have
• Reds, curved lines, too much color.

```html
<!DOCTYPE html>
<html lang="en">
<head>
<meta charset="utf-8">
<title>TOLVARA Communications Brochure</title>
<link href="https://fonts.googleapis.com/css2?family=Source+Sans+3:wght@400;600;700&display=swap" rel="stylesheet">
<style>
:root{
  --ink:#2b2f36;
  --navy:#1f3f8f;
  --brand:#0355a3;
  --sky:#1a8fcc;
  --mid:#1677bd;
  --deep:#1c5aa8;
  --royal:#234a99;
  --charcoal:#3a3b40;
  --logo:#2c3a55;
  --paper:#ffffff;
  --stage:#dcdde0;
}
*{margin:0;padding:0;box-sizing:border-box}
html,body{width:1200px;height:788px;overflow:hidden}
body{background:var(--stage);font-family:"Source Sans 3",Arial,sans-serif;color:var(--ink);position:relative}
.page{position:absolute;top:82px;width:474px;height:613px;background:var(--paper);overflow:hidden;box-shadow:0 3px 10px rgba(0,0,0,.25)}
.page--front{left:80px}
.page--back{left:599px}
.page-art{position:absolute;left:0;top:0}

.brand{position:absolute;left:20px;top:14px;display:flex;align-items:center;gap:8px;color:var(--logo);font-weight:700}
.brand-mark{width:30px;height:30px;background:var(--logo)}
.brand-name{font-size:27px;line-height:23px;letter-spacing:1.5px}
.brand-sub{display:block;font-size:7.4px;line-height:9px;letter-spacing:4.2px;font-weight:600}
.tagline{position:absolute;right:12px;top:18px;font-size:14px;font-weight:600;color:#2c3440}
.tagline b{color:var(--brand);font-weight:700}

.intro{position:absolute;left:13px;top:293px;width:304px;font-size:7px;line-height:10px;text-align:justify}
.band-title{position:absolute;left:44px;top:371px;width:393px;height:18px;line-height:18px;text-align:center;color:#fff;font-size:8.8px}
.features{position:absolute;left:12px;top:389px;width:450px;height:118px;display:flex;box-shadow:0 3px 4px rgba(0,0,0,.2)}
.feature{flex:1;color:#fff;padding:12px 7px 0;text-align:center}
.feature:nth-child(1){background:var(--sky)}
.feature:nth-child(2){background:var(--mid)}
.feature:nth-child(3){background:var(--deep)}
.feature:nth-child(4){background:var(--royal)}
.feature svg{width:24px;height:24px;display:block;margin:0 auto 6px}
.feature h3{font-size:8.8px;font-weight:400;margin-bottom:7px}
.feature p{font-size:7.2px;line-height:8.5px;text-align:justify}
.promise{position:absolute;left:30px;top:518px;width:414px;text-align:center;font-size:8.9px;line-height:11px;color:var(--navy)}

.contact{position:absolute;left:13px;top:566px;list-style:none;color:#fff;font-size:9.6px}
.contact li{display:flex;align-items:center;gap:7px;height:14.5px}
.contact svg{width:9px;height:9px}

.about{position:absolute;left:16px;top:97px;width:176px;color:#fff;font-size:7.6px;line-height:10.1px;text-align:justify}
.about p+p{margin-top:10px}
.proposal-title{position:absolute;left:211px;top:302px;width:232px;height:18px;line-height:18px;text-align:center;color:#fff;font-size:8.8px}
.services{position:absolute;left:225px;top:328px;list-style:none;font-size:9.2px}
.services li{display:flex;align-items:center;gap:8px;height:20.2px}
.services .ico{width:15px;height:15px;border:1px solid var(--logo);border-radius:3px;display:flex;align-items:center;justify-content:center}
.services svg{width:10px;height:10px}
.recovery{position:absolute;left:16px;top:462px;width:172px;font-size:9px;line-height:11.2px;text-align:justify}
</style>
</head>
<body>

<section class="page page--front">
  <svg class="page-art" width="474" height="613" viewBox="0 0 474 613">
    <defs>
      <linearGradient id="windowLight" x1="0" y1="0" x2="1" y2="0">
        <stop offset="0" stop-color="#6c7278"/><stop offset=".3" stop-color="#b9bec3"/><stop offset=".6" stop-color="#e6e9ec"/><stop offset="1" stop-color="#8d939a"/>
      </linearGradient>
      <linearGradient id="roomFloor" x1="0" y1="0" x2="0" y2="1">
        <stop offset="0" stop-color="#3c4046" stop-opacity="0"/><stop offset=".55" stop-color="#3c4046" stop-opacity=".55"/><stop offset="1" stop-color="#2e3237" stop-opacity=".8"/>
      </linearGradient>
      <radialGradient id="deskPhone" cx=".55" cy=".35" r=".7">
        <stop offset="0" stop-color="#5a7a3c"/><stop offset=".35" stop-color="#3d4148"/><stop offset="1" stop-color="#1e2024"/>
      </radialGradient>
    </defs>
    <polygon points="228,64 236,48 474,48 474,64" fill="var(--brand)"/>
    <g role="img" aria-label="Photo of a business team meeting around a boardroom table">
      <rect x="0" y="64" width="474" height="217" fill="url(#windowLight)"/>
      <rect x="0" y="64" width="474" height="217" fill="url(#roomFloor)"/>
    </g>
    <polygon points="316,281 340,258 474,258 474,359 316,359" fill="#fff"/>
    <rect x="340" y="258" width="126" height="98" rx="10" fill="url(#deskPhone)" role="img" aria-label="Photo of a desk IP phone with colour touchscreen"/>
    <polygon points="44,389 56,371 425,371 437,389" fill="var(--charcoal)"/>
    <rect x="0" y="548" width="474" height="65" fill="var(--charcoal)"/>
    <polygon points="276,613 474,567 474,613" fill="var(--royal)"/>
  </svg>

  <div class="brand"><span class="brand-mark"></span><span class="brand-name">TOLVARA<span class="brand-sub">COMMUNICATIONS</span></span></div>
  <div class="tagline">AT <b>TOLVARA</b>, WE MAKE IT EASY.</div>

  <p class="intro">TOLVARA is a Unified Communications platform that breaks down the barriers created by complex on-premise hardware. TOLVARA operates in geo-redundant cloud hubs that are built to protect your business communications from getting disrupted by hardware failures and network outages. Our always-on service provides the ability to increase your users instantly and make changes to your account from anywhere you can access the Internet. TOLVARA delivers the flexibility your business needs in today's business environment.</p>

  <div class="band-title">TOLVARA provides simple to use and reliable PBX service, along with many new features.</div>

  <div class="features">
    <div class="feature">
      <svg viewBox="0 0 24 24" fill="none" stroke="#fff" stroke-width="1.6"><rect x="7" y="2" width="10" height="20" rx="2"/><line x1="11" y1="18.5" x2="13" y2="18.5"/></svg>
      <h3>MOBILE APP</h3>
      <p>Run your business from your mobile phone. Using our mobile app, you can seamlessly move calls from your business line to your cell phone.</p>
    </div>
    <div class="feature">
      <svg viewBox="0 0 24 24" fill="none" stroke="#fff" stroke-width="1.6"><path d="M3 11a7 5 0 1 1 4 4.5L4 18l1-3.5A5 5 0 0 1 3 11z"/><path d="M15 8.5a6 4.5 0 0 1 4 8.5l1 3-3-1.8"/></svg>
      <h3>SMS</h3>
      <p>Activate SMS capabilities to send and receive text messages from your business number!</p>
    </div>
    <div class="feature">
      <svg viewBox="0 0 24 24" fill="none" stroke="#fff" stroke-width="1.6"><rect x="7" y="2" width="10" height="7"/><rect x="4" y="9" width="16" height="12" rx="1.5"/><line x1="8" y1="13" x2="16" y2="13"/><line x1="8" y1="16.5" x2="16" y2="16.5"/></svg>
      <h3>FAX</h3>
      <p>Integrated Fax to email and Fax adapters allow you to eliminate expensive analog lines and improve productivity.</p>
    </div>
    <div class="feature">
      <svg viewBox="0 0 24 24" fill="none" stroke="#fff" stroke-width="1.6"><rect x="2" y="4" width="20" height="13" rx="2"/><circle cx="8" cy="10.5" r="2.5"/><circle cx="16" cy="10.5" r="2.5"/><line x1="8" y1="13" x2="16" y2="13"/><path d="M9 17l-1 4 4-4"/></svg>
      <h3>ENHANCED VOICEMAIL</h3>
      <p>Get voicemails delivered directly to your email or as an SMS message right to your cell phone.</p>
    </div>
  </div>

  <p class="promise">At TOLVARA, we make it easy. Start your service on a 30-day trial, and you will get a professionally installed phone system, including call routing, voice recordings, and user training.</p>

  <ul class="contact">
    <li><svg viewBox="0 0 10 10"><rect width="10" height="10" rx="1.5" fill="#fff"/><path d="M3 2.5l1 1.3-.6.8a4 4 0 0 0 2 2l.8-.6 1.3 1-.6 1C5 8 2 5 2.2 3z" fill="var(--charcoal)"/></svg>555 014 2290</li>
    <li><svg viewBox="0 0 10 10"><rect width="10" height="10" rx="1.5" fill="#fff"/><path d="M2 3h6v4.5H2zM2 3l3 2.5L8 3" fill="none" stroke="var(--charcoal)" stroke-width=".8"/></svg>support@tolvara.com</li>
    <li><svg viewBox="0 0 10 10"><rect width="10" height="10" rx="1.5" fill="#fff"/><circle cx="5" cy="5" r="3" fill="none" stroke="var(--charcoal)" stroke-width=".8"/><path d="M2 5h6M5 2c-1.5 2-1.5 4 0 6M5 2c1.5 2 1.5 4 0 6" fill="none" stroke="var(--charcoal)" stroke-width=".6"/></svg>www.tolvara.com</li>
  </ul>
</section>

<section class="page page--back">
  <svg class="page-art" width="474" height="613" viewBox="0 0 474 613">
    <defs>
      <linearGradient id="streetTone" x1="0" y1="0" x2="1" y2="0">
        <stop offset="0" stop-color="#c8ccd1"/><stop offset=".45" stop-color="#a37a5b"/><stop offset=".7" stop-color="#b98e6e"/><stop offset="1" stop-color="#aeb4ba"/>
      </linearGradient>
      <radialGradient id="streetGlow" cx=".8" cy=".2" r=".6">
        <stop offset="0" stop-color="#f2f3f5" stop-opacity=".7"/><stop offset="1" stop-color="#f2f3f5" stop-opacity="0"/>
      </radialGradient>
      <linearGradient id="appScreens" x1="0" y1="0" x2="1" y2="0">
        <stop offset="0" stop-color="#eef0f3"/><stop offset=".3" stop-color="#d9dce1"/><stop offset=".38" stop-color="#2b2d32"/><stop offset=".7" stop-color="#2b2d32"/><stop offset=".78" stop-color="#dfe3ea"/><stop offset="1" stop-color="#f1f3f7"/>
      </linearGradient>
      <linearGradient id="deviceSet" x1="0" y1="0" x2="1" y2="0">
        <stop offset="0" stop-color="#3a3d43"/><stop offset=".3" stop-color="#4a4e55"/><stop offset=".4" stop-color="#e8ebef"/><stop offset=".82" stop-color="#f3f5f8"/><stop offset=".88" stop-color="#2c2e33"/><stop offset="1" stop-color="#2c2e33"/>
      </linearGradient>
    </defs>
    <polygon points="228,64 236,48 474,48 474,64" fill="var(--brand)"/>
    <rect x="0" y="64" width="474" height="217" fill="var(--charcoal)"/>
    <g role="img" aria-label="Photo of a smiling woman reading messages on her smartphone">
      <polygon points="172,64 474,64 474,281 232,281" fill="url(#streetTone)"/>
      <polygon points="172,64 474,64 474,281 232,281" fill="url(#streetGlow)"/>
    </g>
    <polygon points="150,64 172,64 232,281 210,281" fill="#55565c"/>
    <rect x="22" y="240" width="189" height="174" rx="9" fill="url(#appScreens)" role="img" aria-label="Screens of the mobile and desktop calling app showing dial pad, active call and contacts"/>
    <polygon points="211,320 219,302 443,302 435,320" fill="var(--royal)"/>
    <rect x="198" y="450" width="259" height="112" rx="6" fill="url(#deviceSet)" role="img" aria-label="Desk phone, laptop dashboard and smartphone showing the call analytics portal"/>
    <rect x="0" y="548" width="474" height="65" fill="var(--charcoal)"/>
    <polygon points="276,613 474,567 474,613" fill="var(--royal)"/>
  </svg>

  <div class="brand"><span class="brand-mark"></span><span class="brand-name">TOLVARA<span class="brand-sub">COMMUNICATIONS</span></span></div>
  <div class="tagline">AT <b>TOLVARA</b>, WE MAKE IT EASY.</div>

  <div class="about">
    <p>TOLVARA is a Unified Communications platform that breaks down the barriers created by complex on-premise hardware.</p>
    <p>TOLVARA is deployed in geo-redundant cloud hubs and built to protect your business from getting disrupted by natural disasters and network outages. Our always-on services and agility to grow instantly will deliver the flexibility your business needs.</p>
  </div>

  <div class="proposal-title">Your Proposal Includes the following robust services:</div>
  <ul class="services">
    <li><span class="ico"><svg viewBox="0 0 10 10" fill="none" stroke="#2c3a55" stroke-width=".8"><circle cx="5" cy="5" r="4"/><path d="M1 5h8M5 1c-2 2.5-2 5.5 0 8M5 1c2 2.5 2 5.5 0 8"/></svg></span>Unlimited Local and Domestic Long Distance</li>
    <li><span class="ico"><svg viewBox="0 0 10 10" fill="none" stroke="#2c3a55" stroke-width=".8"><rect x="2.5" y="1" width="5" height="8" rx=".8"/></svg></span>Dedicated Phone Number</li>
    <li><span class="ico"><svg viewBox="0 0 10 10" fill="none" stroke="#2c3a55" stroke-width=".8"><rect x="3" y="1" width="4" height="8" rx=".8"/><line x1="4.5" y1="7.5" x2="5.5" y2="7.5"/></svg></span>Mobile Application</li>
    <li><span class="ico"><svg viewBox="0 0 10 10" fill="none" stroke="#2c3a55" stroke-width=".8"><path d="M5 1l3.5 1.5v2.5C8.5 7 7 8.5 5 9 3 8.5 1.5 7 1.5 5V2.5z"/><path d="M3.5 5l1 1 2-2"/></svg></span>Disaster Recovery is Built-In</li>
    <li><span class="ico"><svg viewBox="0 0 10 10" fill="none" stroke="#2c3a55" stroke-width=".8"><circle cx="5" cy="5" r="1.6"/><path d="M5 1v1.5M5 7.5V9M1 5h1.5M7.5 5H9M2.2 2.2l1 1M6.8 6.8l1 1M7.8 2.2l-1 1M3.2 6.8l-1 1"/></svg></span>Free Professional Installation</li>
  </ul>

  <p class="recovery">Cloud datacenters recovery capabilities. At TOLVARA, we make it easy. Start your service on a 30-day trial, and you will get a professionally installed phone system, including call routing, voice recordings, and user training.</p>

  <ul class="contact">
    <li><svg viewBox="0 0 10 10"><rect width="10" height="10" rx="1.5" fill="#fff"/><path d="M3 2.5l1 1.3-.6.8a4 4 0 0 0 2 2l.8-.6 1.3 1-.6 1C5 8 2 5 2.2 3z" fill="var(--charcoal)"/></svg>555 014 2290</li>
    <li><svg viewBox="0 0 10 10"><rect width="10" height="10" rx="1.5" fill="#fff"/><path d="M2 3h6v4.5H2zM2 3l3 2.5L8 3" fill="none" stroke="var(--charcoal)" stroke-width=".8"/></svg>support@tolvara.com</li>
    <li><svg viewBox="0 0 10 10"><rect width="10" height="10" rx="1.5" fill="#fff"/><circle cx="5" cy="5" r="3" fill="none" stroke="var(--charcoal)" stroke-width=".8"/><path d="M2 5h6M5 2c-1.5 2-1.5 4 0 6M5 2c1.5 2 1.5 4 0 6" fill="none" stroke="var(--charcoal)" stroke-width=".6"/></svg>www.tolvara.com</li>
  </ul>
</section>

</body>
</html>
```